Holiday PROMO Flyer for Healthy Restaurant

Hi ! We need a holiday style promo flyer for Verdana Bowl . Please have a holiday vibe type of design in the background. Include at least 1 of the photos that I provide, and our logo of course. This promo is for a new package that we will be offering until December 31st 2022.

It will have a promo of some type of design that says the following in a creative way:
" HOLIDAY PACKAGE PROMO!"
Buy our holiday package of $500 and receive a $100 gift card!" (THIS SHOULD BE VERY NOTICEABLE AS THIS IS THE ACTUAL PROMO)
Our biggest promo to date.
Offer ends December 31st, 2022.

Take a look at our website to stay consistant with the brand as well.

Industry/Entity Type

Restaurant

Requirements
Must have
• Logo, food photo and gift card photo

```html
<!DOCTYPE html>
<html lang="en">
<head>
<meta charset="utf-8">
<title>Verdana Bowl – Holiday Package Promo</title>
<link rel="stylesheet" href="https://fonts.googleapis.com/css2?family=Montserrat:wght@400;500;700;800&family=Oswald:wght@200&display=swap">
<style>
  :root {
    --stage: #333333;
    --paper: #ffffff;
    --green: #8cc63f;
    --navy: #1b3a66;
    --card-navy: #1c3765;
    --brand-grey: #6d6e71;
    --mist: #d2d2d2;
    --wood-light: #eef0f1;
    --wood-mid: #cfd4d8;
    --sauce: #c84a2c;
    --crust: #d8c6a8;
    --sand: #e6a94b;
    --palm: #3ea33a;
  }
  * { margin: 0; padding: 0; box-sizing: border-box; }
  html, body {
    width: 1200px; height: 1177px; overflow: hidden;
    background: var(--stage);
    font-family: "Montserrat", Arial, sans-serif;
  }
  .flyer {
    position: absolute; left: 264px; top: 82px;
    width: 706px; height: 1002px;
    background: var(--paper); overflow: hidden;
  }
  .flyer > * { position: absolute; }
  .brand { left: 32px; top: 24px; }
  .brand-name {
    font-weight: 800; font-size: 40px; line-height: 1;
    color: var(--brand-grey); letter-spacing: 0.5px; white-space: nowrap;
  }
  .brand-tagline {
    margin-top: 6px; font-weight: 700; font-size: 16px;
    color: var(--green); letter-spacing: 0.3px; white-space: nowrap;
  }
  .palm-leaves { right: 0; top: 0; width: 184px; height: 206px; }
  .headline-holiday {
    left: 82px; top: 100px;
    font-family: "Oswald", "Arial Narrow", sans-serif; font-weight: 200;
    font-size: 116px; line-height: 1; color: var(--mist); letter-spacing: 6px;
    white-space: nowrap;
  }
  .headline-promo {
    left: 32px; top: 210px;
    font-weight: 800; font-size: 52px; line-height: 1; color: var(--green);
    white-space: nowrap;
  }
  .headline-rule {
    left: 32px; top: 264px; width: 506px; height: 2px; background: var(--green);
  }
  .subhead {
    left: 34px; top: 275px;
    font-weight: 700; font-size: 30px; line-height: 1.1; color: var(--navy);
    letter-spacing: 0.6px; white-space: nowrap;
  }
  .offer { right: 46px; top: 328px; text-align: right; z-index: 2; white-space: nowrap; }
  .offer-line {
    font-size: 28px; font-weight: 500; color: var(--navy); letter-spacing: 0.8px; line-height: 1.2;
  }
  .offer-highlight {
    font-size: 28px; font-weight: 800; color: var(--green); letter-spacing: 1px; line-height: 1.2;
  }
  .food-photo { left: 0; top: 340px; width: 706px; height: 420px; }
  .beach-scene { left: 0; top: 740px; width: 400px; height: 262px; }
  .gift-card {
    left: 430px; top: 785px; width: 254px; height: 168px;
    background: var(--card-navy); border-radius: 12px; overflow: hidden;
  }
  .gift-card > * { position: absolute; }
  .ribbon-v { left: 40px; top: 0; width: 10px; height: 100%; background: var(--green); }
  .ribbon-h { left: 0; top: 30px; width: 100%; height: 10px; background: var(--green); }
  .gift-card-label {
    left: 29px; top: 62px; transform-origin: left top; transform: rotate(90deg);
    font-size: 11px; font-weight: 700; color: var(--green); letter-spacing: 1.5px;
    line-height: 1; white-space: nowrap;
  }
  .gift-card-name {
    left: 62px; top: 76px; font-size: 24px; font-weight: 800; line-height: 1;
    color: var(--paper); white-space: nowrap;
  }
  .gift-card-tagline {
    left: 63px; top: 106px; font-size: 10.3px; font-weight: 700; line-height: 1;
    color: var(--green); white-space: nowrap;
  }
  .offer-end {
    left: 420px; top: 958px; width: 274px; text-align: center;
    font-size: 15.5px; font-weight: 800; line-height: 1.15; color: var(--navy);
  }
</style>
</head>
<body>
  <main class="flyer">
    <svg class="food-photo" viewBox="0 0 706 420" role="img" aria-label="Photo of a margherita pizza on parchment paper over white wooden boards">
      <defs>
        <linearGradient id="woodFade" x1="0" y1="0" x2="0" y2="1">
          <stop offset="0" stop-color="#ffffff"/>
          <stop offset="0.18" stop-color="#eef0f1"/>
          <stop offset="1" stop-color="#cfd4d8"/>
        </linearGradient>
        <radialGradient id="pizzaGlow" cx="0.5" cy="0.45" r="0.42">
          <stop offset="0" stop-color="#c84a2c"/>
          <stop offset="0.55" stop-color="#c84a2c" stop-opacity="0.85"/>
          <stop offset="0.75" stop-color="#d8c6a8" stop-opacity="0.7"/>
          <stop offset="1" stop-color="#d8c6a8" stop-opacity="0"/>
        </radialGradient>
      </defs>
      <path d="M0 0 H706 V300 Q353 440 0 300 Z" fill="url(#woodFade)"/>
      <ellipse cx="353" cy="195" rx="260" ry="160" fill="url(#pizzaGlow)"/>
      <path d="M0 320 Q353 455 706 320" fill="none" stroke="#8cc63f" stroke-width="3"/>
    </svg>

    <div class="brand">
      <div class="brand-name">Verdana Bowl</div>
      <div class="brand-tagline">HEALTHY KITCHEN | MEAL PREP</div>
    </div>

    <svg class="palm-leaves" viewBox="0 0 184 206" role="img" aria-label="Tropical palm leaves illustration">
      <defs>
        <linearGradient id="palmTone" x1="1" y1="0" x2="0" y2="1">
          <stop offset="0" stop-color="#3ea33a"/>
          <stop offset="1" stop-color="#7fd16a"/>
        </linearGradient>
      </defs>
      <path d="M184 0 V206 Q120 150 80 70 Q40 40 0 60 Q60 0 184 0 Z" fill="url(#palmTone)" opacity="0.9"/>
    </svg>

    <div class="headline-holiday">HOLIDAY</div>
    <div class="headline-promo">PACKAGE PROMO</div>
    <div class="headline-rule"></div>
    <div class="subhead">OUR BIGGEST PROMO TO DATE</div>

    <div class="offer">
      <div class="offer-line">BUY OUR HOLIDAY PACKAGE OF $500</div>
      <div class="offer-highlight">AND RECEIVE A $100 GIFT CARD!</div>
    </div>

    <svg class="beach-scene" viewBox="0 0 400 262" role="img" aria-label="Illustration of a beach chair, umbrella and cocktail on sand with palm leaves">
      <defs>
        <linearGradient id="beachTone" x1="0" y1="0" x2="1" y2="1">
          <stop offset="0" stop-color="#f2d7c8"/>
          <stop offset="0.5" stop-color="#e6a94b"/>
          <stop offset="1" stop-color="#3ea33a"/>
        </linearGradient>
      </defs>
      <path d="M0 0 Q120 10 180 80 Q300 140 400 262 H0 Z" fill="url(#beachTone)" opacity="0.9"/>
    </svg>

    <div class="gift-card">
      <div class="ribbon-v"></div>
      <div class="ribbon-h"></div>
      <div class="gift-card-label">GIFT CARD</div>
      <div class="gift-card-name">Verdana Bowl</div>
      <div class="gift-card-tagline">HEALTHY KITCHEN | MEAL PREP</div>
    </div>

    <div class="offer-end">OFFER ENDS<br>DECEMBER 31ST, 2022.</div>
  </main>
</body>
</html>
```